Modern Catering Company needs Letterhead Design

We need a letterhead design that will make effective use of the corporate logo and color scheme, along with careful typography, helps this letterhead design communicate the brand well. We do have a corporate logo, however feel free to enhance the color scheme with gold and purple. We are serving a very upscale clientele so the letterhead has to reflect elegance, professionalism, cleanliness, and modern style. We are branding the company so the letterhead and business cards must fit the brand story. There should be no cartoonish elements in the design and we are looking for sharper lines.

Target Market(s)

Businesses and upscale clientele

Industry/Entity Type

Catering

Contact Information for Business Card

while this design can have any number of quirks and distinctions, it needs to be cohesive with the entire brand story clean, professional but edgy

Requirements
Must have
• must have good and carefully placement of it’s logo and where you place the text or the message. Colors blue, very deep purple, jewel tones not pastels, gold. Blue must be the primary color you may accent with purple or gold. Contact information is as follows: Co-Owners/ Chefs: R. Hollowmere & L. Brandt, phone: 414-555-0182 email:Contact@orchardtablecatering.example, address: 6127 W Larkspur Hollow Rd, Milwaukee, WI 53299
Should not have
• pastel colors, Do not add the BBQ information to the letterhead or business card it was a mistake by the previous designer.

```html
<!DOCTYPE html>
<html lang="en">
<head>
<meta charset="utf-8">
<title>Orchard Table Catering – Stationery</title>
<link rel="stylesheet" href="https://fonts.googleapis.com/css2?family=Oswald:wght@300&family=Lato:wght@400;700&display=swap">
<style>
  :root{
    --brand-blue:#0a6cf0;
    --ink:#2b2b2b;
    --muted:#555;
    --paper:#ffffff;
    --rule-grey:#9c9c9c;
    --spine:#1f3f7a;
  }
  *{margin:0;padding:0;box-sizing:border-box}
  html,body{width:1039px;height:1200px;overflow:hidden}
  body{
    position:relative;
    background:linear-gradient(180deg,#5f5f5f 0%,#7b7b7b 45%,#5a5a5a 75%,#2d2d2d 100%);
    font-family:"Lato",sans-serif;color:var(--ink);
  }
  .sheet{position:absolute;background:var(--paper);overflow:hidden}
  .wordmark{font-family:"Oswald",sans-serif;font-weight:300;text-transform:uppercase;line-height:1.05;text-align:center}
  .wordmark span{display:block}

  /* Cover */
  .cover{left:94px;top:121px;width:392px;height:587px;background:var(--brand-blue)}
  .cover .spine{position:absolute;left:22px;top:0;width:4px;height:100%;background:repeating-linear-gradient(180deg,var(--spine) 0 5px,#163162 5px 7px)}
  .cover .wordmark{position:absolute;left:100px;top:10px;width:180px;color:#fff;font-size:27px;letter-spacing:1px}
  .cover .rule{position:absolute;left:26px;right:0;height:3px;background:#fff;clip-path:polygon(0 0,48% 0,47.6% 100%,0 100%,0 0,48.6% 0,100% 0,100% 100%,48.2% 100%)}
  .cover .rule.top{top:80px}
  .cover .rule.bottom{top:543px}

  /* Letterhead */
  .letterhead{left:542px;top:121px;width:392px;height:588px;border:1px solid #ccc}
  .lh-head{position:absolute;left:0;top:0;width:100%;height:56px}
  .lh-sender{position:absolute;left:31px;top:17px;font-size:7px;color:var(--brand-blue);font-weight:700}
  .lh-sender small{display:block;font-size:4.5px;color:#777;font-weight:400;margin-top:2px}
  .letterhead .wordmark{position:absolute;left:150px;top:9px;width:120px;color:var(--brand-blue);font-size:14px}
  .lh-contact{position:absolute;right:22px;top:15px;text-align:right;font-size:5.8px;line-height:9px;color:var(--ink)}
  .lh-contact svg{width:5px;height:5px;vertical-align:-0.5px;margin-left:3px}
  .split-rule{position:absolute;left:0;width:100%;height:4px}
  .split-rule .a,.split-rule .b{position:absolute;top:0;height:100%}
  .lh-rule-top{top:52px}
  .lh-rule-top .a{left:0;width:194px;background:var(--brand-blue);height:3px;top:1px;clip-path:polygon(0 0,100% 0,99% 100%,0 100%)}
  .lh-rule-top .b{left:196px;right:0;background:var(--ink);clip-path:polygon(1% 0,100% 0,100% 100%,0 100%)}
  .lh-rule-bottom{top:552px}
  .lh-rule-bottom .a{left:0;width:195px;background:var(--ink);clip-path:polygon(0 0,100% 0,99% 100%,0 100%)}
  .lh-rule-bottom .b{left:197px;right:0;background:var(--brand-blue);height:3px;top:1px;clip-path:polygon(1% 0,100% 0,100% 100%,0 100%)}
  .lh-body{position:absolute;left:31px;right:27px;top:125px}
  .recipient{font-size:7.6px;line-height:13.6px;color:var(--ink)}
  .recipient strong{font-weight:700}
  .salutation{margin-top:22px;font-size:8.6px;font-weight:700;color:var(--ink)}
  .copy p{font-size:5.2px;line-height:15px;color:var(--muted);text-align:justify;margin-top:6px}
  .copy p+p{margin-top:6px}
  .signoff{position:absolute;left:31px;right:27px;top:440px;font-size:7.6px;color:var(--muted)}
  .signoff .right{position:absolute;right:0;top:0}
  .signoff .lines{margin-top:10px;line-height:15px}
  .lh-footer{position:absolute;left:0;width:100%;top:568px;text-align:center;font-size:5.8px;color:var(--ink)}

  /* Business card */
  .card{left:50px;top:778px;width:453px;height:228px}
  .card .wordmark{position:absolute;left:126px;top:66px;width:200px;color:var(--brand-blue);font-size:29px}
  .card-rule{top:191px}
  .card-rule .a{left:0;width:222px;background:var(--brand-blue);clip-path:polygon(0 0,100% 0,99.4% 100%,0 100%)}
  .card-rule .b{left:224px;right:0;background:var(--rule-grey);clip-path:polygon(0.6% 0,100% 0,100% 100%,0 100%)}
  .card-contact{position:absolute;left:0;width:100%;top:208px;text-align:center;font-size:6.6px;color:var(--ink)}
  .card-contact span{margin:0 12px}
  .card-contact svg{width:6px;height:6px;vertical-align:-1px;margin:0 3px}

  /* Envelope */
  .envelope{left:529px;top:775px;width:463px;height:232px}
  .envelope .flap{position:absolute;left:0;top:0;width:100%;height:52px;background:var(--brand-blue);clip-path:polygon(0 0,100% 0,96.5% 100%,3.5% 100%)}
  .envelope .wordmark{position:absolute;left:0;width:100%;top:116px;color:var(--brand-blue);font-size:28px}
</style>
</head>
<body>

<section class="sheet cover" aria-label="Folder cover">
  <div class="spine"></div>
  <h1 class="wordmark"><span>Orchard Table</span><span>Catering</span></h1>
  <div class="rule top"></div>
  <div class="rule bottom"></div>
</section>

<section class="sheet letterhead" aria-label="Letterhead">
  <header class="lh-head">
    <div class="lh-sender">Martin Hale<small>Managing Director</small></div>
    <div class="wordmark"><span>Orchard Table</span><span>Catering</span></div>
    <div class="lh-contact">
      +1 414 555 0182<svg viewBox="0 0 10 10"><path d="M2 1l2 0 1 2.5-1.3 1a6 6 0 0 0 2.8 2.8l1-1.3L10 7v2a1 1 0 0 1-1 1A9 9 0 0 1 0 1a1 1 0 0 1 1-1z" fill="#0a6cf0"/></svg><br>
      +1 414 555 0182<svg viewBox="0 0 10 10"><path d="M2 1l2 0 1 2.5-1.3 1a6 6 0 0 0 2.8 2.8l1-1.3L10 7v2a1 1 0 0 1-1 1A9 9 0 0 1 0 1a1 1 0 0 1 1-1z" fill="#0a6cf0"/></svg><br>
      Contact@orchardtablecatering.example<svg viewBox="0 0 10 10"><rect x="0" y="2" width="10" height="7" fill="#0a6cf0"/></svg>
    </div>
    <div class="split-rule lh-rule-top"><div class="a"></div><div class="b"></div></div>
  </header>

  <div class="lh-body">
    <address class="recipient" style="font-style:normal">
      <strong>Martin Hale</strong><br>Owner<br>Company Name<br>Address Line1, Address Line2<br>Country -123456
    </address>
    <p class="salutation">Dear Martin Hale</p>
    <div class="copy">
      <p>Lorem ipsum dolor sit amet, consectetur adipiscing elit, sed do eiusmod tempor incididunt ut labore et dolore magna aliqua. Ut enim ad minim veniam, quis nostrud exercitation ullamco laboris nisi ut aliquip ex ea commodo consequat. Duis aute irure dolor in reprehenderit in voluptate velit esse cillum dolore eu fugiat nulla pariatur. Excepteur sint occaecat cupidatat non proident, sunt in culpa qui officia deserunt mollit anim id est laborum.</p>
      <p>Lorem ipsum dolor sit amet, consectetur adipiscing elit, sed do eiusmod tempor incididunt ut labore et dolore magna aliqua. Ut enim ad minim veniam, quis nostrud exercitation ullamco laboris nisi ut aliquip ex ea commodo consequat. Duis aute irure dolor in reprehenderit in voluptate velit esse cillum dolore</p>
      <p>Lorem ipsum dolor sit amet, consectetur adipiscing elit, sed do eiusmod tempor incididunt ut labore et dolore magna aliqua. Ut enim ad minim veniam, quis nostrud exercitation ullamco laboris nisi ut aliquip ex ea commodo consequat. Duis aute irure dolor in reprehenderit in voluptate velit esse cillum dolore eu fugiat nulla pariatur. Excepteur sint occaecat cupidatat non proident, sunt in culpa qui officia deserunt mollit anim id est laborum.</p>
    </div>
  </div>

  <div class="signoff">
    Sincerely,<span class="right">Your Faithfully</span>
    <div class="lines">[ your Name ]<br>[ Title ]</div>
  </div>

  <div class="split-rule lh-rule-bottom"><div class="a"></div><div class="b"></div></div>
  <footer class="lh-footer">6127 W Larkspur Hollow Rd, Milwaukee, WI 53299</footer>
</section>

<section class="sheet card" aria-label="Business card">
  <div class="wordmark"><span>Orchard Table</span><span>Catering</span></div>
  <div class="split-rule card-rule"><div class="a"></div><div class="b"></div></div>
  <div class="card-contact">
    <span>www.orchardtable.example<svg viewBox="0 0 10 10"><circle cx="5" cy="5" r="4.5" fill="#0a6cf0"/></svg></span>
    <span><svg viewBox="0 0 10 10"><path d="M2 1l2 0 1 2.5-1.3 1a6 6 0 0 0 2.8 2.8l1-1.3L10 7v2a1 1 0 0 1-1 1A9 9 0 0 1 0 1a1 1 0 0 1 1-1z" fill="#0a6cf0"/></svg>+1 414 555 0182</span>
  </div>
</section>

<section class="sheet envelope" aria-label="Envelope">
  <div class="flap"></div>
  <div class="wordmark"><span>Orchard Table</span><span>Catering</span></div>
</section>

</body>
</html>
```